Plot Lantern Website Design

At Plot Lantern we’re about to launch an exciting new product in the Project Management space. We aim to simplify the process of reporting on-site work activities. Our flagship product, Briskline, provides users the ability to record work activities as they are performed with automatic reporting back to home base using a smartphone.
The website will be the primary face of the company, and is to be used for advertising the product, for sales, and for subscribers to manage their data. We need a site with a clean, simple appearance that is easy to navigate. To give you a better idea of what we need, our brief includes a wire frame template for the site.
We’d like you to produce a single page site design as shown in the wireframe. We’re looking for a Web 2.0 design and can implement any animation effects that your design needs, just provide us with some notes on how each element should behave. You’re free to design whatever you like within the bounds set out below. After the design is complete the team at Plot Lantern will turn it into a functional website.
-Logo provided. We’d like the website to adhere to work with the logo either using the same colour theme (blue, black, grey) or one you think is complementary.
-Site design to include logo and ‘PlotLantern’ as title at the top of the page.
-Use suitable stock images when you need to place an image.
-Ensure you provide links for the images you use so we can purchase them if we choose.
-Link to hero image example http://www.framevaultpics.example/photo/worker-holding-handset-at-factory-yard-58193047. We aren’t completely happy with this image so we’re open for suggestions of superior images.
-Styling for all visual aspects of the site, including colors, font selection, sizing, placement, shadowing, backgrounds, images, layout, etc.
-Styling of text boxes, ie user login, sign up etc.
-‘Site map’ links at the bottom of page
-Styled form for user sign up, modal acceptable.
link to the Orbix App Bazaar.
-Site may need to be responsive to screen size, mobile, tablet, desktop. Aim for desktop but consider other formats. Styling to accomodate. Please use a standardised grid system.
Target Market(s)
Construction professionals, ie Contract Administrators, Project Managers and trades people
Industry/Entity Type
Advertising
Requirements
Must have
- See brief above
Nice to have
- See brief above
Should not have
- See brief above

```html
<!DOCTYPE html>
<html lang="en">
<head>
<meta charset="utf-8">
<title>PlotLantern</title>
<link rel="stylesheet" href="https://fonts.googleapis.com/css2?family=Lato:wght@400;700;900&display=swap">
<style>
:root{
  --blue:#0c5ea8;
  --blue-deep:#094c89;
  --ink:#222222;
  --muted:#444444;
  --bar:#1c1c1c;
  --bar-field:#0e0e0e;
  --header:#efefef;
  --line:#d8d8d8;
  --field:#f4f4f4;
  --field-line:#cdcdcd;
  --dark:#2a2a2a;
  --dark-low:#3a3a3a;
  --white:#ffffff;
}
*{margin:0;padding:0;box-sizing:border-box}
html,body{width:1200px;height:3120px;overflow:hidden;background:var(--white)}
body{position:relative;font-family:"Lato",Arial,sans-serif;color:var(--ink)}
.abs{position:absolute}

/* top bar */
.topbar{left:0;top:0;width:1200px;height:58px;background:var(--bar)}
.bar-field{height:28px;top:15px;background:var(--bar-field);border-radius:14px;color:#7a7a7a;font-size:10px;line-height:28px;padding-left:14px}
.bar-btn{height:28px;top:15px;background:var(--blue);border-radius:14px;color:var(--white);font-size:11px;font-weight:700;line-height:28px;text-align:center}
.bar-or{top:15px;left:706px;color:var(--white);font-size:11px;font-weight:700;line-height:28px}

/* header */
.header{left:0;top:58px;width:1200px;height:88px;background:var(--header)}
.brand{left:170px;top:82px;display:flex;align-items:center;gap:12px}
.brand-mark{width:40px;height:40px;background:var(--blue)}
.brand-name{font-size:36px;font-weight:900;color:#1d3b63;letter-spacing:-0.5px}
.nav a{position:absolute;top:94px;font-size:15px;font-weight:700;color:var(--ink);text-decoration:none;letter-spacing:.3px}
.nav a.current{color:var(--blue)}
.submenu{left:745px;top:141px;width:112px;height:76px;background:#565656;opacity:.9;z-index:5}
.submenu::before{content:"";position:absolute;left:0;top:0;width:112px;height:5px;background:var(--blue)}
.submenu li{list-style:none;color:var(--white);font-size:10px;margin:20px 0 0 26px;position:relative}
.submenu li+li{margin-top:10px}
.submenu li::before{content:"";position:absolute;left:-10px;top:4px;width:4px;height:4px;border-radius:50%;background:var(--white)}

/* hero */
.hero{left:0;top:146px;width:1200px;height:466px;background:linear-gradient(100deg,#e9e6e0 0%,#cfc6b8 28%,#5a6b86 48%,#3c4f70 62%,#c79a3c 72%,#f2cd1a 84%,#d9a914 100%)}
.dots{left:524px;top:580px;display:flex;gap:10px}
.dots span{width:18px;height:18px;border-radius:50%;background:var(--white)}
.dots span.on{background:var(--blue)}

/* section title */
.section-title{left:0;top:640px;width:1200px;text-align:center;font-size:25px;font-weight:700;letter-spacing:1px}
.rule{left:170px;top:689px;width:860px;height:1px;background:var(--line)}

/* signup */
.signup{left:170px;top:713px;width:356px;height:279px;background:linear-gradient(160deg,#ededed 0%,#b8b8b8 40%,#6f6f6f 100%)}
.signup-title{left:187px;top:834px;font-size:20px;font-weight:700;color:#111}
.signup-input{left:187px;top:866px;width:323px;height:30px;background:#1c1c1c;color:var(--white);font-size:10px;line-height:30px;padding-left:12px}
.signup-btn{left:189px;top:905px;width:92px;height:31px;background:var(--blue);color:var(--white);font-size:13px;line-height:31px;text-align:center}

/* what we do */
.sub-title{font-size:19px;font-weight:700;letter-spacing:.6px}
.video{left:555px;top:753px;width:475px;height:239px;background:linear-gradient(180deg,#4b3a2a 0%,#c4621c 45%,#f29b1e 70%,#5a3a1c 100%)}
.video-play{left:756px;top:828px}
.video-controls{left:594px;top:946px;width:400px;height:14px;background:#222;border-radius:7px}
.video-progress{left:594px;top:946px;width:146px;height:14px;background:var(--blue);border-radius:7px}

/* button row */
.cta{top:1021px;height:59px;background:var(--blue);border-radius:10px;color:var(--white);font-size:14px;font-weight:700;text-align:center;display:flex;flex-direction:column;justify-content:center;box-shadow:0 2px 0 var(--blue-deep)}
.cta small{font-size:9px;font-weight:400}

/* products */
.product-photo{width:180px;height:166px;border:1px solid #e2e2e2}
.product-caption{width:180px;font-size:10.5px;line-height:13px}
.product-caption b{display:block;color:var(--blue);margin-bottom:2px}
.product-caption span{color:var(--muted)}

/* form */
.form-head{left:618px;top:1190px;font-size:11px;font-weight:700}
.progress{left:618px;top:1208px;width:412px;height:28px;background:#e5e5e5;border:1px solid #d0d0d0}
.progress-fill{left:618px;top:1208px;width:135px;height:28px;background:var(--blue);color:var(--white);font-size:9px;line-height:28px;padding-left:10px}
.progress-fill::after{content:"";position:absolute;right:-10px;top:0;border-top:28px solid var(--blue);border-right:10px solid transparent}
.pct{left:746px;top:1258px;font-size:11px}
.label{width:200px;text-align:right;font-size:12px}
.field{height:38px;background:var(--field);border:1px solid var(--field-line)}
.check{left:684px;top:1484px;width:16px;height:16px;border:1px solid #999;background:var(--white)}
.cart{left:855px;top:1470px}
.dropdown{left:811px;top:1520px;width:219px;height:38px;background:var(--field);border:1px solid var(--field-line);font-size:11px;line-height:36px;padding-left:12px}
.submit{left:682px;top:1695px;width:113px;height:34px;background:var(--blue);color:var(--white);font-size:14px;line-height:34px;text-align:center;letter-spacing:1px}

/* welcome */
.welcome-title{left:170px;top:1798px;font-size:21px;font-weight:700;color:var(--blue);letter-spacing:.6px}
.copy{left:170px;width:860px;font-size:12px;line-height:17.6px;color:var(--ink)}

/* customers */
.customers{left:0;top:2165px;width:1200px;height:408px;background:var(--dark)}
.customers-low{left:0;top:2573px;width:1200px;height:131px;background:var(--dark-low)}
.customers-title{left:0;top:2193px;width:1200px;text-align:center;color:var(--white);font-size:21px;font-weight:700;letter-spacing:1.4px}
.grid{left:196px;top:2251px;width:809px;height:391px;display:grid;grid-template-columns:repeat(3,1fr);grid-template-rows:repeat(2,1fr);box-shadow:0 14px 20px rgba(0,0,0,.45)}
.quote-cell{background:#1a1a1a;color:var(--white);font-size:12.5px;line-height:18px;text-align:center;display:flex;flex-direction:column;justify-content:center;padding:0 30px}
.quote-cell b{color:var(--blue);font-weight:700;margin-top:6px}

/* footer */
.sitemap a{position:absolute;font-size:12px;color:var(--ink);text-decoration:none}
.divider{left:713px;top:2725px;width:1px;height:270px;background:var(--line)}
.social{left:736px;top:2752px;display:flex;gap:8px}
.footer-copy{left:736px;top:2812px;width:294px;font-size:10.5px;line-height:20.5px}
.bottom-rule{left:0;top:3033px;width:1200px;height:1px;background:var(--line)}
.legal{left:0;top:3062px;width:1200px;text-align:center;font-size:11px}
</style>
</head>
<body>

<!-- top bar -->
<div class="abs topbar"></div>
<div class="abs bar-field" style="left:170px;width:184px">Search
  <svg class="abs" style="left:160px;top:7px" width="14" height="14" viewBox="0 0 14 14"><circle cx="5.5" cy="5.5" r="4" fill="none" stroke="#fff" stroke-width="2"/><line x1="8.5" y1="8.5" x2="13" y2="13" stroke="#fff" stroke-width="2"/></svg>
</div>
<div class="abs bar-field" style="left:453px;width:160px">Username</div>
<div class="abs bar-btn" style="left:607px;width:80px">LOGIN</div>
<div class="abs bar-or">OR</div>
<div class="abs bar-field" style="left:745px;width:190px">E-Mail Address</div>
<div class="abs bar-btn" style="left:932px;width:98px">GET STARTED</div>

<!-- header -->
<div class="abs header"></div>
<div class="abs brand"><span class="brand-mark"></span><span class="brand-name">PLOTLANTERN</span></div>
<nav class="nav">
  <a class="current" href="#" style="left:753px">BRISKLINE</a>
  <a href="#" style="left:880px">ABOUT</a>
  <a href="#" style="left:953px">SUPPORT</a>
</nav>

<!-- hero -->
<div class="abs hero" role="img" aria-label="Tradesman in a plaid shirt with a tool belt, holding a smartphone and a yellow hard hat"></div>
<div class="abs dots"><span class="on"></span><span></span><span></span><span></span></div>
<ul class="abs submenu"><li>Company</li><li>Press</li></ul>

<!-- intro -->
<h1 class="abs section-title">PLOTLANTERN</h1>
<div class="abs rule"></div>

<div class="abs signup" role="img" aria-label="Black and white photo of a smiling construction crew in hard hats"></div>
<div class="abs signup-title">Sign up now for free!</div>
<div class="abs signup-input">Enter Your E-mail ID</div>
<div class="abs signup-btn">Subscribe</div>

<h2 class="abs sub-title" style="left:555px;top:718px">WHAT WE DO</h2>
<div class="abs video" role="img" aria-label="Video still of an industrial skyline at sunset with a worker holding a yellow hard hat"></div>
<svg class="abs video-play" width="48" height="44" viewBox="0 0 48 44"><rect width="48" height="44" rx="6" fill="#1e1e1e"/><path d="M19 13 L32 22 L19 31 Z" fill="#fff"/></svg>
<div class="abs video-controls"></div>
<div class="abs video-progress"></div>

<a class="abs cta" style="left:170px;width:165px">Get Briskline<small>from the Orbix App Bazaar</small></a>
<a class="abs cta" style="left:358px;width:164px">See Our Pricing</a>
<a class="abs cta" style="left:545px;width:129px">Case Studies</a>
<a class="abs cta" style="left:695px;width:147px">About Us</a>
<a class="abs cta" style="left:865px;width:165px">Contact Us</a>

<!-- featured products -->
<h2 class="abs sub-title" style="left:170px;top:1136px">FEATURED PRODUCTS</h2>

<div class="abs product-photo" style="left:170px;top:1190px;background:linear-gradient(180deg,#f3f3f3,#e8d64a 55%,#333 100%)" role="img" aria-label="Site worker in a hi-vis vest on the phone holding a tablet"></div>
<div class="abs product-caption" style="left:170px;top:1364px"><b>Neque porro quisquam est qui dolorem ipsum quia</b><span>Lorem Ipsum is simply dummy text of the printing and typesetting industry.</span></div>

<div class="abs product-photo" style="left:383px;top:1190px;background:linear-gradient(180deg,#e9e9e9,#8aa0c0 50%,#c2362c 100%)" role="img" aria-label="Engineer in an orange hard hat reviewing a clipboard in front of buildings"></div>
<div class="abs product-caption" style="left:383px;top:1364px"><b>Neque porro quisquam est qui dolorem ipsum quia</b><span>Lorem Ipsum is simply dummy text of the printing and typesetting industry.</span></div>

<div class="abs product-photo" style="left:170px;top:1487px;background:linear-gradient(180deg,#eeeeee,#d8c06a 45%,#2a2a2a 100%)" role="img" aria-label="Construction team in hard hats, one holding a laptop"></div>
<div class="abs product-caption" style="left:170px;top:1664px"><b>Neque porro quisquam est qui dolorem ipsum quia</b><span>Lorem Ipsum is simply dummy text of the printing and typesetting industry.</span></div>

<div class="abs product-photo" style="left:383px;top:1487px;background:linear-gradient(180deg,#8fae6c,#c9c9c9 50%,#3b4560 100%)" role="img" aria-label="Businessman in a suit using a smartphone outdoors"></div>
<div class="abs product-caption" style="left:383px;top:1664px"><b>Neque porro quisquam est qui dolorem ipsum quia</b><span>Lorem Ipsum is simply dummy text of the printing and typesetting industry.</span></div>

<!-- subscription form -->
<div class="abs form-head">Subscription/Payment</div>
<div class="abs progress"></div>
<div class="abs progress-fill">PROGRESS</div>
<div class="abs pct">25%</div>

<div class="abs label" style="left:476px;top:1296px">Company</div>
<div class="abs field" style="left:682px;top:1287px;width:348px"></div>
<div class="abs label" style="left:476px;top:1342px">Name</div>
<div class="abs field" style="left:682px;top:1333px;width:348px"></div>
<div class="abs label" style="left:476px;top:1387px">E-Mail</div>
<div class="abs field" style="left:682px;top:1377px;width:348px"></div>
<div class="abs label" style="left:476px;top:1432px">Phone</div>
<div class="abs field" style="left:682px;top:1423px;width:110px"></div>
<div class="abs" style="left:803px;top:1433px;font-size:11px">Request Call Back</div>

<div class="abs check"><svg width="14" height="14" viewBox="0 0 14 14"><path d="M2 7 L6 11 L12 3" fill="none" stroke="#333" stroke-width="2"/></svg></div>
<div class="abs" style="left:712px;top:1485px;font-size:11px">Check box</div>
<svg class="abs cart" width="40" height="40" viewBox="0 0 40 40"><circle cx="20" cy="20" r="19" fill="var(--blue)"/><path d="M10 13 H14 L17 24 H28 L30 16 H15" fill="none" stroke="#fff" stroke-width="2"/><circle cx="18" cy="28" r="2" fill="#fff"/><circle cx="27" cy="28" r="2" fill="#fff"/></svg>

<div class="abs" style="left:624px;top:1531px;font-size:13px">How did you hear about us</div>
<div class="abs dropdown">Dropdown
  <svg class="abs" style="right:10px;top:10px" width="10" height="16" viewBox="0 0 10 16"><path d="M1 6 L5 1 L9 6 Z M1 10 L5 15 L9 10 Z" fill="#222"/></svg>
</div>

<div class="abs label" style="left:476px;top:1575px">Submit Query</div>
<div class="abs field" style="left:682px;top:1575px;width:348px;height:104px"></div>
<div class="abs submit">SUBMIT</div>

<!-- welcome -->
<h2 class="abs welcome-title">WELCOME TO PLOTLANTERN</h2>
<p class="abs copy" style="top:1835px">Lorem ipsum dolor sit amet, maiores ornare ac fermentum, imperdiet ut vivamus a, nam lectus at nunc. Quam euismod sem, semper ut potenti pellentesque quisque. In eget sapien sed, sit duis vestibulum ultricies, placerat morbi amet vel, nullam in in lorem vel. In molestie elit dui dictum, praesent nascetur pulvinar sed, in dolor pede in aliquam, risus nec error quis pharetra. Eros metus quam augue suspendisse, metus rutrum risus erat in. In ultrices quo ut lectus, etiam vestibulum urna a est, pretium luctus euismod nisl, pellentesque turpis hac ridiculus massa. Venenatis a taciti dolor platea, curabitur lorem platea urna odio, convallis sit pellentesque lacus proin. Et ipsum velit diam nulla, fringilla vel tincidunt vitae, elit turpis tellus vivamus, dictum adipiscing convallis magna id. Viverra eu amet sit, Lorem ipsum dolor sit amet, maiores ornare ac fermentum, imperdiet ut vivamus a, nam lectus at nunc.</p>
<p class="abs copy" style="top:2024px">Quam euismod sem, semper ut potenti pellentesque quisque. In eget sapien sed, sit duis vestibulum ultricies, placerat morbi amet vel, nullam in in lorem vel. In molestie elit dui dictum, praesent nascetur pulvinar sed, in dolor pede in aliquam, risus nec error quis pharetra. Eros metus quam auguesuspendisse, metus rutrum risus erat in. In ultrices quo ut lectus, etiam vestibulum urna a est, pretium luctus euismod nisl, pellentesqueturpis hac ridiculus massa. Venenatis a taciti dolor platea, curabitur lorem platea urna odio, convallis sit pellentesque lacus proin.</p>

<!-- happy customers -->
<div class="abs customers"></div>
<div class="abs customers-low"></div>
<h2 class="abs customers-title">HAPPY CUSTOMERS</h2>
<div class="abs grid">
  <div class="quote-cell">Neque porro quisquam est qui dolorem ipsum quia dolor sit amet, consectetur, adipisci velit...<b>Dorian Kell</b></div>
  <div role="img" aria-label="Smiling man with glasses at an office desk" style="background:linear-gradient(160deg,#c9c9c4,#8a8f94 60%,#5b6068)"></div>
  <div role="img" aria-label="Smiling man with short hair against a light background" style="background:linear-gradient(160deg,#e4e7ea,#b89a82 60%,#6f7378)"></div>
  <div role="img" aria-label="Smiling woman with arms crossed beside a laptop" style="background:linear-gradient(160deg,#efefef,#d9cbb9 55%,#f7f7f7)"></div>
  <div role="img" aria-label="Smiling man outdoors with green foliage behind" style="background:linear-gradient(160deg,#6e8a2e,#a79066 55%,#3e4a2a)"></div>
  <div role="img" aria-label="Woman smiling at her desk in an open office" style="background:linear-gradient(160deg,#d6d6dc,#9aa0b0 55%,#6d5d6a)"></div>
</div>

<!-- footer -->
<nav class="sitemap">
  <a href="#" style="left:170px;top:2751px">About</a>
  <a href="#" style="left:170px;top:2784px">Company</a>
  <a href="#" style="left:170px;top:2815px">Press</a>
  <a href="#" style="left:291px;top:2751px">Briskline</a>
  <a href="#" style="left:291px;top:2784px">Product</a>
  <a href="#" style="left:291px;top:2815px">Pricing</a>
  <a href="#" style="left:291px;top:2849px">Case Studies</a>
  <a href="#" style="left:441px;top:2751px">Support</a>
  <a href="#" style="left:441px;top:2784px">Contact us</a>
  <a href="#" style="left:441px;top:2815px">Terms of use</a>
  <a href="#" style="left:441px;top:2849px">Privacy</a>
  <a href="#" style="left:441px;top:2882px">Help</a>
  <a href="#" style="left:589px;top:2751px">Download</a>
  <a href="#" style="left:589px;top:2784px">Orbix Mobile</a>
</nav>
<div class="abs divider"></div>
<div class="abs social">
  <svg width="36" height="36" viewBox="0 0 36 36"><circle cx="18" cy="18" r="18" fill="var(--blue)"/><path d="M10 18 L18 11 L26 18 M13 16 V25 H23 V16" fill="none" stroke="#fff" stroke-width="2.4"/></svg>
  <svg width="36" height="36" viewBox="0 0 36 36"><circle cx="18" cy="18" r="18" fill="var(--blue)"/><circle cx="12" cy="18" r="3" fill="#fff"/><circle cx="24" cy="11" r="3" fill="#fff"/><circle cx="24" cy="25" r="3" fill="#fff"/><path d="M12 18 L24 11 M12 18 L24 25" stroke="#fff" stroke-width="2"/></svg>
  <svg width="36" height="36" viewBox="0 0 36 36"><circle cx="18" cy="18" r="18" fill="var(--blue)"/><rect x="9" y="12" width="18" height="12" rx="1" fill="#fff"/><path d="M9 12 L18 19 L27 12" fill="none" stroke="var(--blue)" stroke-width="1.6"/></svg>
  <svg width="36" height="36" viewBox="0 0 36 36"><circle cx="18" cy="18" r="18" fill="var(--blue)"/></svg>
</div>
<p class="abs footer-copy">Lorem ipsum dolor sit amet, maiores ornare ac fermentum, imperdiet ut vivamus a, nam lectus at nunc. Quam euismod sem, semper ut potenti pellentesque quisque. In eget sapien sed, sit duis vestibulum ultricies, placerat morbi amet vel, nullam in in lorem vel. In molestie elit dui dictum, praesent nascetur pulvinar sed, in dolor pede in aliquam, risus nec error quis pharetra. Eros metus quam augue suspendisse, metus rutrum risus erat in.</p>
<div class="abs bottom-rule"></div>
<div class="abs legal">© 2014 Company Name ,All Rights Reserved</div>

</body>
</html>
```